Brantley Gutters 15"x12" EDDM flyer

Brantley Gutter a new seamless gutter company is looking for designs for an Every Door Direct Mailing (EDDM) piece. The dimensions will be 15" long and 12" high. Designs must be submitted with pms colors and be at least 300 dpi.

Brantley Gutters LLC.
The products you need at prices you can afford!!!

Brantley Gutters provides an excellent rain gutter system to protect your property. Our “factory on wheels” will custom fit seamless gutters to your home. Our goal is quality craftsmanship with top-notch service at a competitive price. We take pride in our installations, have excellent customer service and guarantee our products and services.

15% off new gutter installations
$50 off gutter repair
$139.00 gutter clean out special. May be additional fee if more than 100 lf. Single story homes only
$99 and up for gutter tune ups. Reseal all end caps and seems, reattach down spouts and align gutters/downspouts

Telephone number: 904-RAINPRO 904-724-7776 I would like the number on there both ways.

Website: brantleygutters-demo.com

We would like a neat, clean design (nothing to busy). I like the color palate of red, white, blue and black.

I have a preference of not having to buy images. Main reason is after going I'll provide my own images.

residential single family homes

neat and clean that states what we do

• Some play on the BG in Brantley Gutters but must be professional. A lot of our clients will call because their wives no longer want them getting up on ladder.

```html
<!DOCTYPE html>
<html lang="en">
<head>
<meta charset="utf-8">
<title>Brantley Gutters – EDDM Mailer</title>
<link rel="stylesheet" href="https://fonts.googleapis.com/css2?family=Arimo:wght@400;700&family=Oswald:wght@700&family=Roboto+Condensed:wght@700&family=Lato:wght@400;700&display=swap">
<style>
  :root {
    --blue: #1f6fe8;
    --red: #ee1c1c;
    --ink: #222222;
    --white: #ffffff;
    --page: #e6e6e6;
    --photo-sky: #9cc3e8;
    --photo-leaf: #5f8a3e;
    --photo-brick: #a86a4e;
  }
  html, body { margin: 0; padding: 0; overflow: hidden; }
  body { width: 900px; height: 1200px; background: var(--page); position: relative; font-family: Arimo, Arial, sans-serif; }
  .card { position: absolute; left: 142px; width: 616px; height: 493px; background: var(--white); box-shadow: 0 2px 8px rgba(0,0,0,.25); overflow: hidden; }
  .card--front { top: 85px; }
  .card--back { top: 620px; }
  .card svg.shapes { position: absolute; inset: 0; }
  .txt { position: absolute; margin: 0; white-space: nowrap; line-height: 1; }

  /* front */
  .brand-name { left: 0; width: 616px; top: 216px; text-align: center; font: 700 36px Arimo, Arial, sans-serif; color: var(--blue); letter-spacing: -0.5px; }
  .brand-tagline { left: 0; width: 616px; top: 257px; text-align: center; font: 400 10.5px Arimo, Arial, sans-serif; color: var(--ink); }
  .headline { left: 18px; top: 285px; font: 700 44px Oswald, sans-serif; color: var(--red); letter-spacing: .3px; line-height: 54px; }
  .subhead { left: 19px; top: 339px; font: 400 29px Arimo, Arial, sans-serif; color: var(--white); }
  .offer-front { left: 405px; width: 211px; top: 287px; text-align: center; font-family: Arimo, Arial, sans-serif; font-weight: 700; }
  .offer-front span { display: block; line-height: 1.02; }
  .offer-front .big { font-size: 28px; color: var(--white); }
  .offer-front .mid { font: 700 28px "Roboto Condensed", sans-serif; color: var(--ink); }
  .offer-front .small { font-size: 20px; color: var(--white); }
  .promise { left: 20px; top: 403px; font: 400 17px Arimo, Arial, sans-serif; color: var(--white); }
  .contact { font: 700 10.5px Lato, sans-serif; color: var(--white); display: flex; align-items: center; gap: 5px; }
  .contact svg { width: 8px; height: 8px; flex: none; }
  .services { left: 250px; top: 450px; font: 700 21px Lato, sans-serif; color: var(--white); display: flex; gap: 14px; }
  .services span::before { content: "»"; color: var(--red); font-size: 26px; margin-right: 9px; position: relative; top: 1px; }

  /* back */
  .burst-text { left: 152px; width: 140px; top: 150px; text-align: center; font-family: Arimo, Arial, sans-serif; font-weight: 700; }
  .burst-text span { display: block; }
  .burst-text .amt { font-size: 28px; color: var(--white); }
  .burst-text .off { font: 700 28px "Roboto Condensed", sans-serif; color: var(--ink); line-height: .95; }
  .burst-text .what { font: 700 14px "Roboto Condensed", sans-serif; color: var(--white); }
  .clean-price { left: 18px; top: 283px; font: 700 24px Arimo, Arial, sans-serif; color: var(--red); }
  .clean-label { left: 18px; top: 310px; font: 700 24px "Roboto Condensed", sans-serif; color: var(--white); line-height: 1.05; }
  .clean-limit { left: 193px; top: 297px; font: 700 19px "Roboto Condensed", sans-serif; color: var(--white); }
  .clean-limit2 { left: 193px; top: 317px; font: 700 20px "Roboto Condensed", sans-serif; color: var(--ink); }
  .tuneup { left: 18px; top: 386px; font: 700 23px "Roboto Condensed", sans-serif; color: var(--ink); }
  .tuneup em { font-style: normal; color: var(--red); }
  .fine-print { left: 18px; top: 424px; width: 296px; white-space: normal; font: 400 4.6px Arimo, Arial, sans-serif; color: var(--ink); line-height: 1.3; }
  .indicia { position: absolute; left: 542px; top: 15px; width: 56px; height: 56px; border: 1px solid #999; font: 400 7.5px Arimo, Arial, sans-serif; text-align: center; line-height: 1.2; padding-top: 3px; box-sizing: border-box; color: var(--ink); }
  .indicia b { font-weight: 700; }
  .address { position: absolute; left: 358px; top: 188px; width: 185px; height: 60px; border: 1px solid var(--ink); box-sizing: border-box; font: 400 11.5px Arimo, Arial, sans-serif; color: var(--ink); padding: 6px 10px; }
  .address .route { font-size: 7.5px; text-align: center; margin-bottom: 10px; }
</style>
</head>
<body>

<section class="card card--front">
  <svg class="shapes" viewBox="0 0 616 493" width="616" height="493">
    <defs>
      <linearGradient id="houseLeft" x1="0" y1="0" x2="0" y2="1">
        <stop offset="0" stop-color="var(--photo-sky)"/><stop offset=".45" stop-color="var(--photo-brick)"/><stop offset="1" stop-color="#c9b9a4"/>
      </linearGradient>
      <linearGradient id="houseMid" x1="0" y1="0" x2="0" y2="1">
        <stop offset="0" stop-color="#4a90e2"/><stop offset=".4" stop-color="var(--photo-leaf)"/><stop offset="1" stop-color="#b9a58a"/>
      </linearGradient>
      <linearGradient id="gutterRight" x1="0" y1="0" x2="1" y2="1">
        <stop offset="0" stop-color="#2f6fd6"/><stop offset="1" stop-color="#e9edf2"/>
      </linearGradient>
    </defs>
    <polygon role="img" aria-label="Photo of a brick house with a red tile roof" points="0,0 38,0 212,158 48,275 0,275" fill="url(#houseLeft)"/>
    <polygon role="img" aria-label="Photo of a large stone family home among trees" points="64,0 552,0 308,188" fill="url(#houseMid)"/>
    <polygon role="img" aria-label="Close-up photo of a white seamless gutter and downspout" points="616,20 616,275 560,275 402,150" fill="url(#gutterRight)"/>
    <polyline points="38,0 212,158 48,275" fill="none" stroke="var(--blue)" stroke-width="7"/>
    <polyline points="20,0 192,158 28,275" fill="none" stroke="var(--blue)" stroke-width="3"/>
    <polyline points="64,0 308,188 552,0" fill="none" stroke="var(--blue)" stroke-width="7"/>
    <polyline points="84,0 308,172 532,0" fill="none" stroke="var(--blue)" stroke-width="2.5"/>
    <polyline points="616,20 402,150 560,275" fill="none" stroke="var(--blue)" stroke-width="7"/>
    <polyline points="616,40 424,155 585,275" fill="none" stroke="var(--blue)" stroke-width="2.5"/>
    <rect x="0" y="275" width="616" height="113" fill="var(--ink)"/>
    <polygon points="440,275 616,275 616,388 440,388 395,331" fill="var(--red)"/>
    <polyline points="428,275 382,331 428,388" fill="none" stroke="var(--white)" stroke-width="8"/>
    <rect x="0" y="388" width="616" height="52" fill="var(--blue)"/>
    <rect x="0" y="440" width="616" height="53" fill="var(--ink)"/>
    <polygon points="0,440 208,440 235,466 208,493 0,493" fill="var(--red)"/>
    <polyline points="218,440 245,466 218,493" fill="none" stroke="var(--white)" stroke-width="6"/>
  </svg>

  <p class="txt brand-name">Brantley Gutters</p>
  <p class="txt brand-tagline">PERFORMS TUNE UPS TO SEAMLESS GUTTERS</p>
  <h1 class="txt headline">WE ONLY INSTALL</h1>
  <p class="txt subhead">6" K STYLE GUTTERS</p>
  <p class="txt offer-front"><span class="big">15% OFF</span><span class="mid">New gutter</span><span class="small">Installations</span></p>
  <p class="txt promise">We will come out and custom build seamless gutters to form your home</p>
  <p class="txt contact" style="left:18px;top:451px;">
    <svg viewBox="0 0 10 10"><path d="M2 1 L4 1 L4.6 3 L3.4 4 Q4.5 6 6 6.6 L7 5.4 L9 6 L9 8 Q8 9 6.5 8.7 Q2 7 1.2 3 Q1 1.8 2 1Z" fill="#fff"/></svg>904-RAINPRO | 904-724-7776</p>
  <p class="txt contact" style="left:18px;top:470px;">
    <svg viewBox="0 0 10 10"><circle cx="5" cy="5" r="4.5" fill="#fff"/></svg>www.brantleygutters-demo.com</p>
  <p class="txt services"><span>Installs</span><span>Repairs</span><span>Cleans</span></p>
</section>

<section class="card card--back">
  <svg class="shapes" viewBox="0 0 616 493" width="616" height="493">
    <defs>
      <linearGradient id="workerPhoto" x1="0" y1="0" x2="1" y2="1">
        <stop offset="0" stop-color="var(--photo-leaf)"/><stop offset=".55" stop-color="#2f4f8a"/><stop offset="1" stop-color="#8e9aa6"/>
      </linearGradient>
    </defs>
    <polygon role="img" aria-label="Photo of a gutter technician in gloves cleaning a roof gutter" points="0,0 160,0 262,95 145,215 0,215" fill="url(#workerPhoto)"/>
    <polyline points="170,0 274,98 152,222" fill="none" stroke="var(--blue)" stroke-width="7"/>
    <rect x="0" y="218" width="140" height="9" fill="var(--blue)"/>
    <g transform="translate(222 185)" fill="var(--red)">
      <rect x="-52" y="-52" width="104" height="104"/>
      <rect x="-52" y="-52" width="104" height="104" transform="rotate(22.5)"/>
      <rect x="-52" y="-52" width="104" height="104" transform="rotate(45)"/>
      <rect x="-52" y="-52" width="104" height="104" transform="rotate(67.5)"/>
    </g>
    <rect x="0" y="275" width="182" height="92" fill="var(--ink)"/>
    <polygon points="186,275 322,275 322,345 186,345 156,310" fill="var(--blue)"/>
    <polyline points="178,275 148,310 178,345" fill="none" stroke="var(--white)" stroke-width="7"/>
    <rect x="321" y="0" width="3" height="455" fill="var(--red)"/>
    <rect x="325" y="0" width="3" height="455" fill="var(--blue)"/>
    <rect x="0" y="455" width="341" height="38" fill="var(--ink)"/>
  </svg>

  <p class="txt burst-text"><span class="amt">$50</span><span class="off">OFF</span><span class="what">Gutter Repairs</span></p>
  <p class="txt clean-price">$139.00</p>
  <p class="txt clean-label">For Gutter<br>Cleaning</p>
  <p class="txt clean-limit">100 Linear feet</p>
  <p class="txt clean-limit2">1st story only</p>
  <p class="txt tuneup">Gutter Tune ups starting at <em>$99</em></p>
  <p class="txt fine-print">Your Gutter Tune up includes resealing all end caps and seams, reattaching downspouts and aligning gutters and downspouts. Cleaning covers up to 100 linear feet; additional fee may apply. Single story homes only.</p>
  <p class="txt contact" style="left:18px;top:461px;font-size:11px;">
    <svg viewBox="0 0 10 10"><path d="M2 1 L4 1 L4.6 3 L3.4 4 Q4.5 6 6 6.6 L7 5.4 L9 6 L9 8 Q8 9 6.5 8.7 Q2 7 1.2 3 Q1 1.8 2 1Z" fill="#ee1c1c"/></svg>904-RAINPRO | 904-724-7776</p>
  <p class="txt contact" style="left:18px;top:477px;font-size:11px;">
    <svg viewBox="0 0 10 10"><circle cx="5" cy="5" r="4.5" fill="#ee1c1c"/></svg>www.brantleygutters-demo.com</p>

  <div class="indicia">PRSRT STD<br>ECRWSS<br>U.S. POSTAGE<br><b>PAID</b><br>EDDM RETAIL</div>
  <div class="address">
    <div class="route">*****************ECRWSS****</div>
    Local<br>Postal Customer
  </div>
</section>

</body>
</html>
```